Need DL Flyer for Real Estate Drops

We need a real estate flyer ,double sided. With content on 1 side like: Want to know what's your house is worth " contact us today and on other side agent details. We are looking for an ongoing partnership with designer so this assignment will be ongoing

```html
<!DOCTYPE html>
<html lang="en">
<head>
<meta charset="utf-8">
<title>Dunecrest Real Estate – DL Flyer</title>
<link href="https://fonts.googleapis.com/css2?family=Poppins:wght@300;400;500;600;700;800&display=swap" rel="stylesheet">
<style>
  :root{
    --navy:#1c2257;
    --red:#c8202b;
    --red-deep:#b81f3a;
    --ink:#1a1a1a;
    --body:#444;
    --white:#ffffff;
    --backdrop:#c4c4c4;
    --rule:#dcdcdc;
  }
  *{box-sizing:border-box;margin:0;padding:0}
  html,body{width:769px;height:1200px;overflow:hidden}
  body{background:var(--backdrop);font-family:'Poppins',sans-serif;position:relative}
  .sheet-frame{position:absolute;top:367px;width:360px;height:466px;overflow:hidden;box-shadow:0 2px 6px rgba(0,0,0,.15)}
  .sheet-frame.back{left:14px}
  .sheet-frame.front{left:394px}
  .sheet{position:absolute;left:0;top:0;width:560px;height:725px;background:var(--white);transform:scale(.643);transform-origin:0 0}
  .sheet > svg.shapes{position:absolute;left:0;top:0;width:560px;height:725px}
  .abs{position:absolute}

  /* footer */
  .footer-item{position:absolute;top:676px;display:flex;gap:8px;color:var(--white);font-size:10px;line-height:1.45}
  .footer-item strong{display:block;font-weight:600;font-size:10.5px}
  .footer-item svg{width:13px;height:13px;margin-top:3px;flex:none}
  .footer-item.office{left:196px}
  .footer-item.call{left:412px}

  /* back side */
  .agency-title{left:45px;top:252px;color:var(--red);font-size:22px;font-weight:500}
  .about{left:45px;width:470px;color:var(--body);font-size:9.6px;line-height:15px}
  .about.first{top:290px}
  .about.second{top:364px}
  .agent-name{left:45px;top:464px;color:var(--navy);font-size:30px;font-weight:600;letter-spacing:.3px}
  .agent-role{left:45px;top:506px;color:var(--ink);font-size:13px;font-weight:600;line-height:15px}
  .contact-list{left:45px;top:566px;list-style:none}
  .contact-list li{display:flex;align-items:center;gap:6px;font-size:11px;font-weight:500;color:var(--ink);height:21px}
  .contact-list svg{width:11px;height:11px;flex:none}
  .social-dot{position:absolute;border-radius:50%;width:30px;height:30px}
  .social-dot.one{left:306px;top:497px;background:var(--red)}
  .social-dot.two{left:287px;top:534px;background:var(--navy)}

  /* front side */
  .brand{left:45px;top:30px;display:flex;align-items:center;gap:10px}
  .brand-mark{width:32px;height:32px;background:var(--red)}
  .brand-name{color:var(--navy);font-size:29px;font-weight:500;letter-spacing:.2px}
  .branch{left:327px;top:33px;font-size:9.5px;line-height:13px;color:var(--ink);font-weight:500}
  .branch strong{display:block;color:var(--red);font-weight:500;font-size:10px}
  .pride{left:47px;top:128px;color:var(--white)}
  .pride .lead{font-size:18px;font-weight:300;letter-spacing:.3px;line-height:22px}
  .pride .big{font-size:29px;font-weight:800;line-height:29px;letter-spacing:.5px}
  .pride .soft{font-size:20px;font-weight:300;line-height:24px}
  .pride-note{left:47px;top:243px;width:140px;color:var(--white);font-size:9.5px;line-height:11.5px}
  .selling{left:0;width:560px;top:347px;text-align:center;color:var(--ink);font-size:21px;font-weight:500}
  .selling-copy{left:70px;width:420px;top:384px;text-align:center;color:var(--body);font-size:9.6px;line-height:15px}
  .latest{left:45px;top:440px;color:var(--red);font-size:22px;font-weight:800;letter-spacing:.2px}
  .listing{position:absolute;top:480px;width:148px}
  .listing-card{width:148px;height:118px;background:var(--white);box-shadow:0 1px 5px rgba(0,0,0,.18);padding:7px;position:relative}
  .listing-photo{width:134px;height:104px;background:linear-gradient(180deg,#5f6570 0%,#8b8f96 38%,#e9e6e0 40%,#d9d4cb 70%,#a89272 100%)}
  .listing-tag{position:absolute;left:3px;top:3px;width:34px;height:16px;background:var(--red);clip-path:polygon(0 60%,60% 0,100% 0,0 100%)}
  .listing-address{margin-top:10px;font-size:8.5px;font-weight:700;line-height:10.5px;color:var(--ink);text-transform:uppercase}
</style>
</head>
<body>

<!-- Agent side -->
<div class="sheet-frame back">
  <section class="sheet agent-side">
    <svg class="shapes" viewBox="0 0 560 725" aria-hidden="true">
      <polygon points="517,0 560,0 560,245 360,245" fill="var(--red)"/>
      <polygon points="560,360 560,660 350,660" fill="var(--red)"/>
      <line x1="0" y1="556" x2="285" y2="556" stroke="var(--rule)" stroke-width="1.5"/>
      <polygon points="0,652 155,652 198,725 0,725" fill="var(--navy)"/>
      <polygon points="162,660 560,660 560,725 204,725" fill="var(--red-deep)"/>
      <polygon points="162,660 420,660 420,725 204,725" fill="var(--red)"/>
    </svg>
    <div class="abs" role="img" aria-label="Bright open-plan living and dining room with timber floor"
         style="left:0;top:0;width:517px;height:230px;background:linear-gradient(160deg,#f2f2f0 0%,#e4e2dd 45%,#c79a6c 80%,#a8744a 100%);clip-path:polygon(0 0,100% 0,380px 230px,0 230px)"></div>
    <div class="abs" role="img" aria-label="Portrait of the agent in a suit"
         style="left:268px;top:440px;width:285px;height:160px;background:linear-gradient(135deg,#f4e6e1 0%,#d9c7c0 60%,#8e8a8c 100%);clip-path:polygon(30px 0,285px 0,190px 160px,0 160px)"></div>

    <h1 class="abs agency-title">Dunecrest Real Estate</h1>
    <p class="abs about first">Dunecrest Real Estate was established in 2017 and has a dynamic team of sales and rentals. We are committed to the continuous professional development of all our team and employ the latest technology tools to provide an accurate, timely experience for our clients.</p>
    <p class="abs about second">Our office is based in Westfield and deals in western and northern suburbs of Melbourne. We take pride in providing excellent customer service and will always strive to make your search for the perfect property as seamless as straightforward and stress-free as possible. Dunecrest Real Estate has a broad selection of residential and rural real estate to suit all budgets.</p>

    <h2 class="abs agent-name">Rohan Mehta</h2>
    <p class="abs agent-role">Managing Director/LEA,<br>Dunecrest Real Estate</p>
    <span class="social-dot one"></span>
    <span class="social-dot two"></span>

    <ul class="abs contact-list">
      <li><svg viewBox="0 0 12 12"><rect x="3" y="0.5" width="6" height="11" rx="1" fill="none" stroke="var(--ink)" stroke-width="1.2"/><circle cx="6" cy="9.5" r=".7" fill="var(--ink)"/></svg>0412345678</li>
      <li><svg viewBox="0 0 12 12"><rect x="0.5" y="2" width="11" height="8" fill="var(--ink)"/><polyline points="0.5,2 6,6.5 11.5,2" fill="none" stroke="#fff" stroke-width="1"/></svg>rohan@dunecrestrealty.com.au</li>
      <li><svg viewBox="0 0 12 12"><circle cx="6" cy="6" r="5" fill="none" stroke="var(--ink)" stroke-width="1.1"/><ellipse cx="6" cy="6" rx="2.2" ry="5" fill="none" stroke="var(--ink)" stroke-width="1"/><line x1="1" y1="6" x2="11" y2="6" stroke="var(--ink)"/></svg>www.dunecrestrealty.com.au</li>
    </ul>

    <div class="footer-item office">
      <svg viewBox="0 0 12 12"><path d="M6 .5a4 4 0 0 1 4 4c0 3-4 7-4 7s-4-4-4-7a4 4 0 0 1 4-4z" fill="#fff"/><circle cx="6" cy="4.5" r="1.5" fill="var(--red)"/></svg>
      <div><strong>HEAD OFFICE</strong>14/8 Harbour Rd, Westfield, VIC 3000</div>
    </div>
    <div class="footer-item call">
      <svg viewBox="0 0 12 12"><path d="M2.5 1l2 2-1 1.5c.8 1.6 2 2.8 3.5 3.5L8.5 7l2 2-1.5 2C4.5 10.5 1.5 7.5 1 3z" fill="#fff"/></svg>
      <div><strong>CALL</strong>(03) 9000 1234</div>
    </div>
  </section>
</div>

<!-- Listings side -->
<div class="sheet-frame front">
  <section class="sheet listings-side">
    <svg class="shapes" viewBox="0 0 560 725" aria-hidden="true">
      <polygon points="495,87 560,0 560,87" fill="var(--red)"/>
      <polygon points="0,87 310,87 180,325 0,325" fill="var(--navy)"/>
      <polygon points="0,325 57,325 0,408" fill="var(--red)"/>
      <polygon points="0,652 155,652 198,725 0,725" fill="var(--navy)"/>
      <polygon points="162,660 560,660 560,725 204,725" fill="var(--red-deep)"/>
      <polygon points="162,660 420,660 420,725 204,725" fill="var(--red)"/>
    </svg>
    <div class="abs" role="img" aria-label="Dining table with cushioned chairs beside a garden window"
         style="left:180px;top:87px;width:380px;height:238px;background:linear-gradient(150deg,#a9b79a 0%,#dfe3df 35%,#c9b7a0 60%,#8a5a36 100%);clip-path:polygon(130px 0,380px 0,380px 238px,0 238px)"></div>
    <svg class="abs" style="left:0;top:0" width="560" height="725" viewBox="0 0 560 725" aria-hidden="true">
      <polygon points="262,175 276,175 194,325 180,325" fill="var(--red)"/>
      <line x1="0" y1="226" x2="248" y2="226" stroke="#fff" stroke-width="1"/>
      <line x1="268" y1="456" x2="445" y2="456" stroke="var(--red)" stroke-width="1.5"/>
      <circle cx="445" cy="456" r="4.5" fill="var(--red)"/>
    </svg>

    <div class="abs brand"><span class="brand-mark"></span><span class="brand-name">dunecrest</span></div>
    <p class="abs branch"><strong>BRANCH OFFICE</strong>88 Station St, Northvale, VIC 3000</p>

    <div class="abs pride">
      <p class="lead">WE TAKE PRIDE IN</p>
      <p class="big">PROVIDING</p>
      <p class="big">EXCELLENT</p>
      <p class="soft">customer</p>
    </div>
    <p class="abs pride-note">Our team is waiting to help you, click below to get in touch.</p>

    <h2 class="abs selling">Selling A Property?</h2>
    <p class="abs selling-copy">In case you're planning to sell a property, contact us and we make sure to get the best possible conditions for you. Setting up the exposé and professional Areal estate photography are free of charge.</p>

    <h3 class="abs latest">LATEST FOR SALE</h3>

    <article class="listing" style="left:45px">
      <div class="listing-card"><div class="listing-photo" role="img" aria-label="New single-storey home exterior"></div><span class="listing-tag"></span></div>
      <p class="listing-address">12 Sunrise Drive,<br>Oakridge Park</p>
    </article>
    <article class="listing" style="left:205px">
      <div class="listing-card"><div class="listing-photo" role="img" aria-label="New single-storey home exterior"></div><span class="listing-tag"></span></div>
      <p class="listing-address">Lot 2210 Meadow Loop,<br>Greenvale</p>
    </article>
    <article class="listing" style="left:365px">
      <div class="listing-card"><div class="listing-photo" role="img" aria-label="New single-storey home exterior"></div><span class="listing-tag"></span></div>
      <p class="listing-address">27 Kestrel Drive,<br>Elmwood</p>
    </article>

    <div class="footer-item office">
      <svg viewBox="0 0 12 12"><path d="M6 .5a4 4 0 0 1 4 4c0 3-4 7-4 7s-4-4-4-7a4 4 0 0 1 4-4z" fill="#fff"/><circle cx="6" cy="4.5" r="1.5" fill="var(--red)"/></svg>
      <div><strong>HEAD OFFICE</strong>14/8 Harbour Rd, Westfield, VIC 3000</div>
    </div>
    <div class="footer-item call">
      <svg viewBox="0 0 12 12"><path d="M2.5 1l2 2-1 1.5c.8 1.6 2 2.8 3.5 3.5L8.5 7l2 2-1.5 2C4.5 10.5 1.5 7.5 1 3z" fill="#fff"/></svg>
      <div><strong>CALL</strong>(03) 9000 1234</div>
    </div>
  </section>
</div>

</body>
</html>
```